Kestrel Builders Business Card Design Project

Clean sharp business card
Ability to write on back of card
Details for the card -
Address: PO Box 5867, Tingapla, Qld, 4173
ABN: 47 305 961 220
BSA LIC 2650874
Ph: 07 3562 4470
Fax: 07 3562 4475
Email: kestrelbuilders@mailbrook.com.au

```html
<!DOCTYPE html>
<html lang="en">
<head>
<meta charset="utf-8">
<title>Kestrel Builders – Business Card</title>
<link rel="stylesheet" href="https://fonts.googleapis.com/css2?family=Lora:wght@400;500&display=swap">
<style>
  :root {
    --backdrop: #a9aaac;
    --card-dark: #000000;
    --card-light: #ffffff;
    --silver: #c8c9cb;
    --graphite: #5f6062;
    --text-grey: #4a4a4a;
    --orange: #f28a1c;
    --white: #ffffff;
  }
  * { margin: 0; padding: 0; box-sizing: border-box; }
  html, body {
    width: 1200px;
    height: 847px;
    overflow: hidden;
    background: var(--backdrop);
    font-family: "Lora", Georgia, serif;
  }
  .canvas {
    position: relative;
    width: 1200px;
    height: 847px;
  }
  .card {
    position: absolute;
  }

  /* Front of card */
  .card--front {
    left: 144px;
    top: 98px;
    width: 593px;
    height: 339px;
    background: var(--card-dark);
  }
  .front-brand {
    position: absolute;
    left: 0;
    right: 0;
    top: 128px;
    display: flex;
    align-items: center;
    justify-content: center;
    gap: 18px;
  }
  .front-brand__dot {
    width: 22px;
    height: 22px;
    border-radius: 50%;
    background: var(--orange);
  }
  .front-brand__name {
    font-size: 52px;
    font-weight: 400;
    color: var(--silver);
    line-height: 1;
  }
  .front-email {
    position: absolute;
    left: 0;
    right: 0;
    top: 302px;
    text-align: center;
    font-size: 17px;
    color: var(--white);
  }

  /* Back of card */
  .card--back {
    left: 484px;
    top: 448px;
    width: 591px;
    height: 336px;
    background: var(--card-light);
  }
  .back-brand {
    position: absolute;
    left: 36px;
    top: 118px;
    width: 210px;
    display: flex;
    align-items: center;
    gap: 10px;
  }
  .back-brand__dot {
    flex: none;
    width: 14px;
    height: 14px;
    border-radius: 50%;
    background: var(--orange);
  }
  .back-brand__name {
    font-size: 30px;
    font-weight: 400;
    color: var(--graphite);
    line-height: 1.1;
  }
  .divider {
    position: absolute;
    left: 277px;
    top: 49px;
    width: 10px;
    height: 256px;
  }
  .holder {
    position: absolute;
    left: 389px;
    top: 16px;
    text-align: right;
    color: var(--graphite);
  }
  .holder__name {
    font-size: 22px;
    font-weight: 400;
    letter-spacing: 0.3px;
  }
  .holder__role {
    font-size: 13px;
    margin-top: -2px;
    margin-right: -14px;
  }
  .details {
    position: absolute;
    left: 346px;
    top: 134px;
    list-style: none;
    font-size: 13px;
    line-height: 18px;
    color: var(--text-grey);
  }
  .back-email {
    position: absolute;
    left: 346px;
    top: 268px;
    font-size: 12.5px;
    letter-spacing: -0.2px;
    color: var(--text-grey);
  }
</style>
</head>
<body>
<main class="canvas">

  <section class="card card--front" aria-label="Card front">
    <div class="front-brand">
      <span class="front-brand__dot"></span>
      <span class="front-brand__name">Kestrel Builders</span>
    </div>
    <p class="front-email">Email:kestrelbuilders@mailbrook.com.au</p>
  </section>

  <section class="card card--back" aria-label="Card back">
    <div class="back-brand">
      <span class="back-brand__dot"></span>
      <span class="back-brand__name">Kestrel Builders</span>
    </div>

    <svg class="divider" viewBox="0 0 10 256" aria-hidden="true">
      <rect x="0" y="0" width="3" height="256" fill="var(--graphite)"/>
      <rect x="5" y="0" width="3" height="256" fill="var(--orange)"/>
    </svg>

    <div class="holder">
      <p class="holder__name">YOUR NAME</p>
      <p class="holder__role">Managing Director</p>
    </div>

    <ul class="details">
      <li>ADD:PO Box 5867,Harrowvale,Vic,3981</li>
      <li>ABN:47 305 961 220</li>
      <li>BSA LIC:2650874</li>
      <li>PH:07 3562 4470</li>
      <li>FAX:07 3562 4475</li>
    </ul>

    <p class="back-email">Email:kestrelbuilders@mailbrook.com.au</p>
  </section>

</main>
</body>
</html>
```